Bathroom, Plumbing & TIling Business

I require a business card design for me new business the 'Larkmoor Bathroom Company', based in Melbourne, Victoria.

Specialising in bathroom refurbishments, new installations, repairs, plumbing and tiling, the Larkmoor Bathroom Company provides a professional high-quality standard of workmanship, creating your dream.

With over 15 years’ experience in the bathroom and plumbing industry the LBC will only take payment once the job is completed to the customers’ satisfaction*. We pride ourselves on hard-work, professionalism, customer service and always delivering that high end finish you have only dreamt of.

The majority of our work, to date, has come through personal recommendation and word-of-mouth and as a family-run company we do not pressure sell or push our customers to have unnecessary works.

The Larkmoor Bathroom Company can source products for our customers at trade price and will always quote a job realistically, and honestly, on the work and materials required. We always let the customer know how long the job will take and we will complete it within the specified time.

LBC are dedicated to fitting new bathrooms, renovations, waterproofing, shower repairs/leaks and tiling to removing and refitting bathrooms, ensuites and showers and installing plumbing systems.

The business cards for LBC need to be clean, modern and simple. White matt finish with embossed bath logo.

On side 1 of the card we require the words 'Larkmoor Bathroom Company' to be written in the Anson font with the letter L,B and C a lot larger in size to the other letters. The letter 'y' (at the end of the word 'Company') is to follow under the title in a curved bath shape growing up and around the letter L to a shower head dripping water in to the letter 'L' which will be half filled with water. The colour for the main title is the green colour which is used in the Waterfall colour scheme on MS Publisher. The tag line, 'Creating your Dream', is to be situated in a smaller font size, underneath the main title in the Anson font and be written in black (we think).

Side 2 of the card is to have a smaller sized version of the Side 1 logo (but only saying LBC - not the full title, Larkmoor Bathroom Company) situated at the top and contact details (again, in the Anson font underneath.

The final design should communicate high-end, high quality and professionalism of bathroom fitting and plumbing works.
Updates

Hi there

Please could you include/list some of the services, provided by LBC on the back of the card:

Bathroom Renovations

Bathroom Installations

Tiling

Shower Repairs

Plumbing

Cheers :-)

Target Market(s)

Home owners, renters, property developers, rental companies seeking anything works related to bathrooms, plumbing and tiling. Age range from 21-70.

Industry/Entity Type

Industry

Requirements
Must have
• Double sided business card
Side 1: main - title (Larkmoor Bathroom Company), logo (bath & shower) and tag line (Creating your Dream)
Side 2: Smaller sized version of Side 1 (but only with the letters LBC - not the whole company name) and contact details:

Tobias Whitcombe (Owner)
Brackenvale, 3821

Website: www.larkmoorbathroomcompany.com.au
Email: Tobias@lbc-example.com.au
Phone: +61 418 357 902
Nice to have
• The business cards for LBC need to be clean, modern and simple. White/or off white matt finish with embossed bath logo.

Should not have
• We do not want to see any of the following on the card:

No garish colours
No clip art
No cartoon images of people, baths or plumbing tools
No small photographs of bathrooms or other 'photographic' images

```html
<!DOCTYPE html>
<html lang="en">
<head>
<meta charset="utf-8">
<title>Larkmoor Bathroom Company – Business Card Back</title>
<link rel="stylesheet" href="https://fonts.googleapis.com/css2?family=Montserrat:wght@400;500&family=Poiret+One&display=swap">
<style>
  :root {
    --paper: #ffffff;
    --teal: #699d99;
    --ink: #111111;
    --ink-soft: #223232;
    --brand: #1c1c1c;
  }
  html, body {
    margin: 0;
    padding: 0;
    overflow: hidden;
    background: var(--paper);
  }
  .card {
    position: relative;
    width: 1200px;
    height: 600px;
    overflow: hidden;
    background: var(--paper);
    font-family: "Montserrat", Arial, sans-serif;
  }
  .card-header {
    position: absolute;
    inset: 0 0 auto 0;
    height: 166px;
    background: var(--paper);
  }
  .brand-mark {
    position: absolute;
    left: 162px;
    top: 56px;
    display: flex;
    align-items: center;
    gap: 14px;
  }
  .brand-dot {
    width: 22px;
    height: 22px;
    border-radius: 50%;
    background: var(--teal);
  }
  .brand-name {
    font-family: "Montserrat", Arial, sans-serif;
    font-weight: 500;
    font-size: 42px;
    letter-spacing: 1px;
    color: var(--brand);
    line-height: 1;
  }
  .contact {
    position: absolute;
    left: 462px;
    top: 0;
    margin: 0;
    font-style: normal;
    font-size: 21px;
    line-height: 29px;
    color: var(--ink);
  }
  .contact p { margin: 0; }
  .contact .gap { margin-top: 17px; }
  .services {
    position: absolute;
    inset: 166px 0 0 0;
    background: var(--teal);
  }
  .services-title {
    position: absolute;
    left: 165px;
    top: 18px;
    margin: 0;
    font-family: "Poiret One", "Century Gothic", sans-serif;
    font-weight: 400;
    font-size: 44px;
    letter-spacing: 1px;
    color: var(--ink-soft);
  }
  .services-list {
    position: absolute;
    left: 162px;
    top: 84px;
    margin: 0;
    padding: 0;
    list-style: none;
    font-size: 20px;
    color: var(--ink-soft);
  }
  .services-list li {
    height: 46px;
    letter-spacing: 0.5px;
  }
</style>
</head>
<body>
  <main class="card">
    <header class="card-header">
      <div class="brand-mark">
        <span class="brand-dot"></span>
        <span class="brand-name">Larkmoor</span>
      </div>
      <address class="contact">
        <p>Tobias Whitcombe (Owner)</p>
        <p>Brackenvale, 3821</p>
        <p class="gap">Website: www.larkmoorbathroomcompany.com.au</p>
        <p>Email: Tobias@lbc-example.com.au</p>
        <p>Phone: +61 418 357 902</p>
      </address>
    </header>
    <section class="services">
      <h2 class="services-title">Services, Provided by LBC</h2>
      <ul class="services-list">
        <li>Bathroom Renovations</li>
        <li>Bathroom Installations</li>
        <li>Tiling</li>
        <li>Shower Repairs</li>
        <li>Plumbing</li>
      </ul>
    </section>
  </main>
</body>
</html>
```